Plumbing Company After Business Card

Business card for a plumbing business that offers a variety of plumbing services including maintenance, domestic and commercial plumbing. My main focus is to offer high quality professional service. A logo on the card would be ideal. Any other questions feel free to email. Cheers

Looking for something modern and upmarket with preferably a matte black background

Business name is Keystone Plumbing and Gas

Industry/Entity Type

Plumbing

Contact Information for Business Card

Keystone Plumbing and Gas
Marcus Thornell
0427915368
14 Corrigan Road, Elmvale 3561
keystoneplumbing@mailbay.com.au
ABN 52 647 183 925

Font styles to use
Sans Serif

Colors
1b1b1b
ffffff
3377b5

Requirements
Must have
• Domestic
• Commercial
• Maintenance

```html
<!DOCTYPE html>
<html lang="en">
<head>
<meta charset="utf-8">
<title>Keystone Plumbing and Gas – Business Card</title>
<link rel="stylesheet" href="https://fonts.googleapis.com/css2?family=Anton&family=Open+Sans:wght@400;600;700&display=swap">
<style>
  :root {
    --matte-black: #1b1b1b;
    --white: #ffffff;
    --brand-blue: #3377b5;
    --blue-shade: #2c6aa6;
    --soft-white: #cfd8e2;
    --frame-line: #555555;
  }
  * { margin: 0; padding: 0; box-sizing: border-box; }
  html, body { width: 1021px; height: 1200px; overflow: hidden; background: var(--white); }
  .sheet {
    position: relative;
    width: 1021px;
    height: 1200px;
    border: 1.5px solid var(--frame-line);
    background: var(--white);
    font-family: "Open Sans", sans-serif;
    color: var(--white);
  }
  .card {
    position: absolute;
    left: 26px;
    width: 969px;
    height: 553px;
    overflow: hidden;
  }
  .card--front { top: 29px; background: var(--matte-black); }
  .card--back { top: 617px; background: var(--brand-blue); }

  .brand { position: absolute; text-align: center; color: var(--white); font-weight: 600; }
  .brand__mark { display: block; margin: 0 auto; border-radius: 50%; }
  .brand__name { display: block; text-transform: uppercase; letter-spacing: 0.12em; line-height: 1; }
  .brand__tagline { display: block; line-height: 1; }

  .card--front .brand { left: 0; right: 0; top: 150px; }
  .card--front .brand__mark { width: 120px; height: 120px; background: var(--brand-blue); margin-bottom: 34px; }
  .card--front .brand__name { font-size: 58px; }
  .card--front .brand__tagline { font-size: 21px; margin-top: 12px; }

  .services {
    position: absolute;
    left: 0; right: 0; bottom: 46px;
    text-align: center;
    font-size: 15px;
    letter-spacing: 0.28em;
    text-transform: uppercase;
    color: var(--soft-white);
  }
  .services__dot { color: var(--brand-blue); margin: 0 10px; }

  .card--back .brand { left: 100px; width: 260px; top: 232px; }
  .card--back .brand__mark { width: 110px; height: 110px; background: var(--white); margin-bottom: 30px; }
  .card--back .brand__name { font-size: 42px; }
  .card--back .brand__tagline { font-size: 17px; margin-top: 10px; }

  .backdrop-word {
    position: absolute;
    left: -2px;
    top: -22px;
    white-space: nowrap;
    font-family: "Anton", sans-serif;
    font-size: 100px;
    line-height: 1;
    letter-spacing: 0.02em;
    color: var(--blue-shade);
    transform: scaleX(1.36);
    transform-origin: left top;
  }

  .contact { position: absolute; left: 447px; top: 210px; }
  .contact__name { font-size: 40px; font-weight: 700; line-height: 1; letter-spacing: -0.01em; transform: scaleX(0.92); transform-origin: left; }
  .contact__role, .contact__abn { font-size: 29px; line-height: 1; margin-top: 15px; }
  .contact__list { list-style: none; margin-top: 22px; }
  .contact__item { display: flex; align-items: center; font-size: 27px; line-height: 1; height: 43px; }
  .contact__icon { width: 30px; height: 30px; margin-right: 14px; flex: none; }
</style>
</head>
<body>
  <main class="sheet">
    <section class="card card--front">
      <div class="brand">
        <span class="brand__mark"></span>
        <span class="brand__name">Keystone</span>
        <span class="brand__tagline">Plumbing and Gas</span>
      </div>
      <p class="services">Domestic<span class="services__dot">•</span>Commercial<span class="services__dot">•</span>Maintenance</p>
    </section>

    <section class="card card--back">
      <div class="backdrop-word" aria-hidden="true">PLUMBING AND GAS</div>

      <div class="brand">
        <span class="brand__mark"></span>
        <span class="brand__name">Keystone</span>
        <span class="brand__tagline">Plumbing and Gas</span>
      </div>

      <div class="contact">
        <p class="contact__name">Marcus Thornell</p>
        <p class="contact__role">Founder</p>
        <p class="contact__abn">ABN 52 647 183 925</p>
        <ul class="contact__list">
          <li class="contact__item">
            <svg class="contact__icon" viewBox="0 0 32 32" fill="none" stroke="#ffffff" stroke-width="1.6" stroke-linejoin="round">
              <path d="M21 4l6 6-4 4-3-3-9 9 3 3-4 4-6-6c0-9 8-17 17-17z"/>
            </svg>
            0427 915 368
          </li>
          <li class="contact__item">
            <svg class="contact__icon" viewBox="0 0 32 32" fill="none" stroke="#ffffff" stroke-width="1.6" stroke-linejoin="round">
              <rect x="5" y="9" width="22" height="15"/>
              <path d="M5 9l11 9 11-9M5 24l8-8M27 24l-8-8"/>
            </svg>
            keystoneplumbing@mailbay.com.au
          </li>
          <li class="contact__item">
            <svg class="contact__icon" viewBox="0 0 32 32" fill="none" stroke="#ffffff" stroke-width="1.6" stroke-linejoin="round">
              <path d="M3 16L16 4l13 12M7 13v15h7v-8h4v8h7V13M22 8V4h3v7"/>
            </svg>
            14 Corrigan Road, Elmvale 3561
          </li>
        </ul>
      </div>
    </section>
  </main>
</body>
</html>
```